Residential improvers, A Quiet Harbor 9 Me *

Quiet Harbor 9 Me is a real estate company specializing in turning unloved properties into improved, happy places to live. We specialize in thoughtfully-improved residential properties for buyers or renters. Our company needs a business card that reflects the renovated homes we create using green and Feng Shui principles,

Please disregard the images we submitted. We are looking for an abstract, sophisticated elegant design. No eggs in a nest ... nothing cute. The image can be soft.
Updates

Aloha (hello) all designers. We are a serious property investment/improvement company. We strive to be unique, renovating with style and elegance. Our business card must portray the same message. We thought the nest and flower might be "it" ... clearly it's not, once we saw what you submitted. Please revisit the brief as it was modified yesterday. Mahalo for your input! We look forward to hearing from all designers that have been invited.

Industry/Entity Type

Real Estate Development

Contact Information for Business Card

We will have separate business cards for
1) Corabeth Danvers 808-555-0173 corabeth@mailtrove.net
2) Trina Vasquell 808-555-0196 trinavasquell@mailtrove.net
** can we add the website later ... in the process of approval.
Investors * Renovators * Connectors

Font styles to use
Sans Serif

Colors
cadf82

Requirements
Must have
• a feng shui feel ... modern. Color - green with black print.
Nice to have
• A Quiet Harbor 9 Me

```html
<!DOCTYPE html>
<html lang="en">
<head>
<meta charset="utf-8">
<title>Quiet Harbor 9 Me — Business Card</title>
<link rel="stylesheet" href="https://fonts.googleapis.com/css2?family=Montserrat:wght@600;700&family=Quicksand:wght@400;500&display=swap">
<style>
  :root {
    --backdrop: #3a3b3d;
    --leaf: #9ccb3b;
    --leaf-soft: #cadf82;
    --ink: #231f20;
    --paper: #ffffff;
    --rule: #9ccb3b;
  }
  * { margin: 0; padding: 0; box-sizing: border-box; }
  html, body {
    width: 1200px;
    height: 900px;
    overflow: hidden;
    background: var(--backdrop);
  }
  .stage {
    position: relative;
    width: 1200px;
    height: 900px;
  }
  .card {
    position: absolute;
    width: 560px;
    height: 320px;
    border-radius: 24px;
    overflow: hidden;
  }

  /* Front: green side */
  .card-front {
    left: 90px;
    top: 110px;
    background: var(--leaf);
  }
  .card-front .tint {
    position: absolute;
    inset: 0;
    width: 100%;
    height: 100%;
  }
  .card-front .bar {
    position: absolute;
    height: 9px;
    background: var(--ink);
  }
  .card-front .bar-top { right: 0; top: 182px; width: 170px; }
  .card-front .bar-bottom { left: 0; bottom: 58px; width: 200px; }
  .card-front .brand {
    position: absolute;
    left: 0; right: 0;
    top: 104px;
    text-align: center;
    font-family: "Quicksand", sans-serif;
    font-weight: 500;
    font-size: 34px;
    line-height: 44px;
    color: var(--ink);
  }
  .card-front .website {
    position: absolute;
    left: 212px;
    bottom: 52px;
    font-family: "Montserrat", sans-serif;
    font-weight: 700;
    font-size: 17px;
    line-height: 20px;
    color: var(--ink);
  }

  /* Back: white side */
  .card-back {
    left: 550px;
    top: 470px;
    background: var(--paper);
  }
  .card-back .brand {
    position: absolute;
    left: 40px;
    top: 150px;
    display: flex;
    align-items: center;
    gap: 10px;
    font-family: "Quicksand", sans-serif;
    font-weight: 500;
    font-size: 24px;
    line-height: 30px;
    color: var(--ink);
  }
  .card-back .brand-dot {
    width: 16px;
    height: 16px;
    border-radius: 50%;
    background: var(--leaf);
    flex: none;
  }
  .card-back .contact {
    position: absolute;
    left: 310px;
    top: 56px;
    font-family: "Quicksand", sans-serif;
    color: var(--ink);
  }
  .card-back .person {
    font-family: "Montserrat", sans-serif;
    font-weight: 700;
    font-size: 19px;
  }
  .card-back .person-rule {
    width: 52px;
    height: 3px;
    background: var(--rule);
    margin: 14px 0 18px 30px;
  }
  .card-back .line {
    font-size: 16px;
    line-height: 22px;
    padding-left: 30px;
  }
  .card-back .rule-side {
    position: absolute;
    right: 0;
    top: 172px;
    width: 110px;
    height: 3px;
    background: var(--rule);
  }
  .card-back .tagline {
    position: absolute;
    left: 250px;
    top: 222px;
    font-family: "Quicksand", sans-serif;
    font-weight: 500;
    font-size: 16px;
    color: var(--ink);
  }
  .card-back .rule-bottom {
    position: absolute;
    left: 0;
    bottom: 46px;
    width: 230px;
    height: 3px;
    background: var(--rule);
  }
</style>
</head>
<body>
<main class="stage">
  <section class="card card-front">
    <svg class="tint" viewBox="0 0 560 320" preserveAspectRatio="none" aria-hidden="true">
      <polygon points="300,0 560,0 560,320 420,320" fill="#cadf82"/>
    </svg>
    <div class="brand">Quiet Harbor 9 Me</div>
    <div class="bar bar-top"></div>
    <div class="bar bar-bottom"></div>
    <div class="website">www.QuietHarbor9Me.com</div>
  </section>

  <section class="card card-back">
    <div class="brand"><span class="brand-dot"></span>Quiet Harbor 9 Me</div>
    <div class="contact">
      <div class="person">Corabeth Danvers</div>
      <div class="person-rule"></div>
      <div class="line">808-555-0173</div>
      <div class="line">corabeth@mailtrove.net</div>
    </div>
    <div class="rule-side"></div>
    <div class="tagline">Investors * Renovators * Connectors</div>
    <div class="rule-bottom"></div>
  </section>
</main>
</body>
</html>
```